Rising Paths Web Design

I am starting a new company that will provide LIFE COACHING services - I have tried to design a website, but it's too complicated. Right now, it's just me - I'm the only person that will provide services through the website - I have used artmarket to purchase a logo (see below). I want to be able to update the website myself, but need a template - basic design. Because I am not technologically savvy enough to explain in words - I basically want to have a website that will provide basic information about my services (coaching), a page about me and my background, hopefully scheduling possibilities, and testimonials — also a page for writing/blogs. I bought a website through NetHarbor - so when I have a template, I guess I”d use that - but maybe I’ll need to work with a designer to actually get it up on the internet. I have a head shot that I’ll upload, too.
Target Market(s)
Clients from the independent (private school) world - teachers, administrators
Number of Pages Required
4 page
Look and feel
Each slider illustrates characteristics of the customer's brand and the style your logo design should communicate.

```html
<!DOCTYPE html>
<html lang="en">
<head>
<meta charset="utf-8">
<title>Rising Paths – My Blogs</title>
<link rel="stylesheet" href="https://fonts.googleapis.com/css2?family=Poppins:wght@400;500;600&family=Open+Sans:wght@400;600&display=swap">
<style>
  :root {
    --teal: #00ae8f;
    --ink: #2b2b2b;
    --text: #555555;
    --card-bg: #f6f9f8;
    --card-line: #e4ecea;
    --white: #ffffff;
  }
  * { box-sizing: border-box; margin: 0; padding: 0; }
  html, body { width: 791px; height: 1200px; overflow: hidden; background: var(--white); }
  body { position: relative; font-family: "Open Sans", sans-serif; color: var(--text); }

  .brand { position: absolute; left: 78px; top: 8px; width: 90px; height: 64px; }
  .brand-ring { position: absolute; left: 0; top: 0; width: 62px; height: 62px; border: 1px solid var(--teal); border-radius: 50%; }
  .brand-name { position: absolute; left: 5px; top: 30px; font-family: "Poppins", sans-serif; font-weight: 500; font-size: 8.5px; color: var(--teal); white-space: nowrap; letter-spacing: 0.2px; }

  .main-nav { position: absolute; top: 31px; right: 78px; display: flex; align-items: center; font-family: "Poppins", sans-serif; font-size: 7.5px; color: var(--ink); }
  .main-nav a { color: inherit; text-decoration: none; margin-left: 34px; line-height: 19px; }
  .main-nav a.is-pill { border: 1px solid var(--teal); border-radius: 10px; padding: 0 14px; margin-left: 20px; }
  .main-nav a.is-pill + a { margin-left: 20px; }

  .page-title { position: absolute; left: 78px; top: 106px; font-family: "Poppins", sans-serif; font-weight: 600; font-size: 31px; color: #3a3a3a; line-height: 40px; }
  .intro { position: absolute; left: 78px; top: 152px; width: 545px; font-size: 8.4px; line-height: 16.6px; color: var(--text); }

  .filters { position: absolute; left: 78px; top: 227px; display: flex; gap: 14px; }
  .filter { width: 92px; height: 24px; border: 1px solid var(--teal); border-radius: 12px; font-family: "Poppins", sans-serif; font-size: 8px; color: var(--ink); display: flex; align-items: center; justify-content: center; }
  .filter.is-active { background: var(--teal); color: var(--white); }

  .blog-grid { position: absolute; left: 78px; top: 276px; width: 636px; display: grid; grid-template-columns: repeat(3, 191px); column-gap: 31px; row-gap: 21px; }
  .post { height: 226px; background: var(--card-bg); border: 1px solid var(--card-line); text-align: center; padding-top: 15px; }
  .post-media { width: 160px; height: 111px; margin: 0 auto; }
  .media-study { background: linear-gradient(160deg, #c9a27c 0%, #9c8a6e 35%, #6f9a3e 70%, #5d8e2c 100%); }
  .media-meeting { background: linear-gradient(110deg, #e6e8ec 0%, #cfd3da 45%, #2e3a55 80%, #1f2a40 100%); }
  .media-field { background: linear-gradient(180deg, #f2f1ee 0%, #ebe6dc 55%, #d2a858 78%, #b4883a 100%); }
  .post-title { margin-top: 15px; font-family: "Poppins", sans-serif; font-weight: 600; font-size: 11.2px; color: var(--ink); }
  .post-excerpt { margin-top: 7px; font-family: "Poppins", sans-serif; font-size: 7.2px; line-height: 14px; color: var(--text); padding: 0 18px; }
  .post-link { display: block; margin-top: 8px; font-weight: 600; font-size: 8.8px; color: var(--ink); text-decoration: none; }

  .site-footer { position: absolute; left: 0; top: 1061px; width: 791px; height: 139px; background: var(--teal); color: var(--white); }
  .social { position: absolute; top: 35px; left: 343px; display: flex; gap: 11px; }
  .social span { width: 18px; height: 18px; border: 1px solid var(--white); border-radius: 50%; }
  .footer-nav { position: absolute; top: 71px; left: 0; width: 791px; display: flex; justify-content: center; gap: 28px; font-size: 7.5px; }
  .footer-nav a { color: var(--white); text-decoration: none; }
  .copyright { position: absolute; top: 100px; width: 791px; text-align: center; font-size: 6.5px; }
</style>
</head>
<body>
  <header>
    <div class="brand">
      <span class="brand-ring"></span>
      <span class="brand-name">RISING PATHS</span>
    </div>
    <nav class="main-nav">
      <a href="#">Home</a>
      <a href="#">About Me</a>
      <a href="#">Schedule a Appointment</a>
      <a href="#" class="is-pill">Testimonials</a>
      <a href="#">My Blogs</a>
    </nav>
  </header>

  <main>
    <h1 class="page-title">My Blogs</h1>
    <p class="intro">Lorem ipsum dolor sit amet, consectetur adipiscing elit, sed do eiusmod tempor incididunt ut labore et dolore magna aliqua. Ut enim ad minim veniam, quis nostrud exercitation ullamco laboris nisi ut aliquip ex ea commodo consequat. Duis aute irure dolor in reprehenderit in voluptate velit esse cillum dolore eu fugiat nulla pariatur. Excepteur sint occaecat cupidatat</p>

    <div class="filters">
      <span class="filter is-active">All Category</span>
      <span class="filter">Category 01</span>
      <span class="filter">Category 02</span>
      <span class="filter">Category 03</span>
    </div>

    <section class="blog-grid">
      <article class="post"><div class="post-media media-study" role="img" aria-label="Photo of a smiling woman lying on grass with a book"></div><h2 class="post-title">Sed ut perspiciatis unde..</h2><p class="post-excerpt">Lorem ipsum dolor sit amet, consectetur adipiscing elit, sed do eiusmod.</p><a class="post-link" href="#">Read More</a></article>
      <article class="post"><div class="post-media media-meeting" role="img" aria-label="Photo of three people shaking hands at a meeting table"></div><h2 class="post-title">Sed ut perspiciatis unde..</h2><p class="post-excerpt">Lorem ipsum dolor sit amet, consectetur adipiscing elit, sed do eiusmod.</p><a class="post-link" href="#">Read More</a></article>
      <article class="post"><div class="post-media media-field" role="img" aria-label="Photo of a woman with raised arms in a golden field"></div><h2 class="post-title">Sed ut perspiciatis unde..</h2><p class="post-excerpt">Lorem ipsum dolor sit amet, consectetur adipiscing elit, sed do eiusmod.</p><a class="post-link" href="#">Read More</a></article>
      <article class="post"><div class="post-media media-study" role="img" aria-label="Photo of a smiling woman lying on grass with a book"></div><h2 class="post-title">Sed ut perspiciatis unde..</h2><p class="post-excerpt">Lorem ipsum dolor sit amet, consectetur adipiscing elit, sed do eiusmod.</p><a class="post-link" href="#">Read More</a></article>
      <article class="post"><div class="post-media media-meeting" role="img" aria-label="Photo of three people shaking hands at a meeting table"></div><h2 class="post-title">Sed ut perspiciatis unde..</h2><p class="post-excerpt">Lorem ipsum dolor sit amet, consectetur adipiscing elit, sed do eiusmod.</p><a class="post-link" href="#">Read More</a></article>
      <article class="post"><div class="post-media media-field" role="img" aria-label="Photo of a woman with raised arms in a golden field"></div><h2 class="post-title">Sed ut perspiciatis unde..</h2><p class="post-excerpt">Lorem ipsum dolor sit amet, consectetur adipiscing elit, sed do eiusmod.</p><a class="post-link" href="#">Read More</a></article>
      <article class="post"><div class="post-media media-study" role="img" aria-label="Photo of a smiling woman lying on grass with a book"></div><h2 class="post-title">Sed ut perspiciatis unde..</h2><p class="post-excerpt">Lorem ipsum dolor sit amet, consectetur adipiscing elit, sed do eiusmod.</p><a class="post-link" href="#">Read More</a></article>
      <article class="post"><div class="post-media media-meeting" role="img" aria-label="Photo of three people shaking hands at a meeting table"></div><h2 class="post-title">Sed ut perspiciatis unde..</h2><p class="post-excerpt">Lorem ipsum dolor sit amet, consectetur adipiscing elit, sed do eiusmod.</p><a class="post-link" href="#">Read More</a></article>
      <article class="post"><div class="post-media media-field" role="img" aria-label="Photo of a woman with raised arms in a golden field"></div><h2 class="post-title">Sed ut perspiciatis unde..</h2><p class="post-excerpt">Lorem ipsum dolor sit amet, consectetur adipiscing elit, sed do eiusmod.</p><a class="post-link" href="#">Read More</a></article>
    </section>
  </main>

  <footer class="site-footer">
    <div class="social">
      <span role="img" aria-label="Social network link"></span>
      <span role="img" aria-label="Social network link"></span>
      <span role="img" aria-label="Social network link"></span>
      <span role="img" aria-label="Social network link"></span>
    </div>
    <nav class="footer-nav">
      <a href="#">Home</a>
      <a href="#">About Me</a>
      <a href="#">Schedule a Appointment</a>
      <a href="#">Testimonials</a>
      <a href="#">My Blogs</a>
    </nav>
    <p class="copyright">2022 All rights reserved</p>
  </footer>
</body>
</html>
```